WP website design (Bellwether)

We need a wordpress design for an established auction and real estate company based in Arkansas. The winning design will incorporate a professional color scheme with company logo in a clean layout. The design needs to consider that this will be developed on a responsive theme.

Industry/Entity Type

Real Estate

Font styles to use
Sans Serif

Colors

Designer to choose colors to be used in the design.

Requirements
Must have
• Site will have slideshow, please use stock real estate or other image. A rough idea of homepage content is attached - not necessarily for design purposes.

Navigation Structure is:
1) Home
2) Auctions
3) Services
4) For Sale
5) About Us
6) Reid Videos
7) News & Events
8) Contact Us

Widgets will include:
Social media icons (Facebook, Youtube, RSS)
Testimonials Widget - this should be prominent
Featured Video
Email Signup form (Sign up to receive exclusive email updates for Bellwether auctions. )
Nice to have
• A drop down menu example
Should not have
• no gavel in the design

```html
<!DOCTYPE html>
<html lang="en">
<head>
<meta charset="utf-8">
<title>Bellwether Auction &amp; Marketing</title>
<link href="https://fonts.googleapis.com/css2?family=Open+Sans:ital,wght@0,400;0,600;0,700;1,400;1,600&family=Roboto+Condensed:wght@400;700&display=swap" rel="stylesheet">
<style>
:root{
  --green:#008a3e;
  --green-dark:#006b30;
  --ink:#333333;
  --muted:#555555;
  --page:#eeeeee;
  --panel:#f6f6f6;
  --white:#ffffff;
  --line:#cfcfcf;
  --sky:#1da1f2;
}
*{box-sizing:border-box;margin:0;padding:0}
html,body{width:1200px;height:2317px;overflow:hidden}
body{background:var(--page);font-family:"Open Sans",sans-serif;color:var(--ink);position:relative}
.wrap{width:1068px;margin:0 auto;position:relative;height:100%}
.cond{font-family:"Roboto Condensed",sans-serif}

/* header */
.site-header{height:154px;background:linear-gradient(#e8e8e8,#f2f2f2)}
.brand{position:absolute;left:0;top:18px;width:343px;height:136px;background:var(--white);border-radius:14px 14px 0 0;box-shadow:0 0 4px rgba(0,0,0,.15);display:flex;flex-direction:column;justify-content:center;padding-left:20px}
.brand-name{font-family:"Open Sans",sans-serif;font-weight:700;font-size:36px;color:#1d1d1d;letter-spacing:.5px;line-height:1}
.brand-tag{font-family:"Open Sans",sans-serif;font-weight:700;font-size:13px;color:#1d1d1d;margin-top:6px;padding-left:12px}
.social{position:absolute;right:0;top:20px;display:flex;gap:16px}
.social span{width:38px;height:38px;border-radius:50%;background:#3a3a3a;border:3px solid #ddd;box-shadow:0 0 0 1px #999}
.social span:first-child{background:#1b75bb}
.contact{position:absolute;right:0;top:88px;display:flex;gap:22px;align-items:center;font-family:"Roboto Condensed",sans-serif;font-size:24px;color:#444}
.contact div{display:flex;align-items:center;gap:10px}

/* nav */
.main-nav{height:54px;background:#f4f4f4;border-top:1px solid #ddd;border-bottom:1px solid #ddd}
.main-nav ul{list-style:none;display:flex;height:100%}
.main-nav li{font-family:"Roboto Condensed",sans-serif;font-size:23px;font-weight:700;color:#333;display:flex;align-items:center;padding:0 16px;border-right:1px solid #e0e0e0;background:linear-gradient(#fafafa,#ececec)}
.main-nav li.active{background:var(--green);color:#fff;padding:0 29px}

/* slider */
.hero{height:535px;position:relative;background:linear-gradient(180deg,#b8d5ec 0%,#e3eef6 45%,#d7e2c8 70%,#3d3d3d 100%)}
.hero-photo{position:absolute;inset:0;background:linear-gradient(120deg,#c9dbe9 0%,#e8eef2 35%,#9fbf7a 55%,#2f2f2f 80%)}
.hero-caption{position:absolute;left:0;right:0;top:210px;text-align:center;font-family:"Roboto Condensed",sans-serif;font-weight:700;font-size:40px;color:var(--green);text-shadow:-2px -2px 0 #fff,2px -2px 0 #fff,-2px 2px 0 #fff,2px 2px 0 #fff}
.hero-arrow{position:absolute;top:205px}

/* welcome */
.welcome{height:310px;background:var(--panel)}
.welcome h2{position:absolute;top:42px;left:0;font-family:"Roboto Condensed",sans-serif;font-size:26px;color:var(--green);width:623px;padding-bottom:8px;border-bottom:1px dotted #bbb}
.welcome p{position:absolute;top:90px;left:0;width:623px;font-size:14.5px;line-height:28px;color:var(--muted)}
.go{width:28px;height:28px;border-radius:50%;background:var(--green);display:flex;align-items:center;justify-content:center}
.welcome .go{position:absolute;left:0;top:253px}
.video{position:absolute;right:0;top:37px;width:422px;height:242px;border:5px solid var(--green);background:linear-gradient(160deg,#1b2236,#3a4660 60%,#151a28);display:flex;align-items:center;justify-content:center}

/* testimonials */
.testimonials{height:334px;background:var(--white)}
.section-title{font-family:"Roboto Condensed",sans-serif;font-weight:700;font-size:26px;color:var(--green);display:flex;align-items:center;gap:10px}
.testimonials .section-title{position:absolute;top:18px;left:0;width:710px}
.testimonials .section-title::after{content:"";flex:1;border-bottom:3px dotted #ccc}
.t-photo{position:absolute;left:22px;top:93px;width:150px;height:140px;background:linear-gradient(#dcdcdc,#3a3a3a 70%,#222);border:1px solid #999}
.t-name{position:absolute;left:193px;top:52px;font-style:italic;font-weight:600;font-size:20px;color:var(--green)}
.t-lead{position:absolute;left:196px;top:86px;width:510px;font-size:16px;line-height:24px;color:#111}
.t-quote{position:absolute;left:193px;top:140px;width:518px;font-style:italic;font-size:12.5px;line-height:26px;color:#555}
.btn-sm{display:inline-flex;align-items:center;justify-content:center;background:var(--green);color:#fff;font-style:italic;font-size:11px;width:99px;height:25px}
.testimonials .btn-sm{position:absolute;left:611px;top:277px}
.signup{position:absolute;right:0;top:22px;width:322px;height:281px;background:#fff;box-shadow:0 0 6px rgba(0,0,0,.18);padding:18px 22px}
.signup h3{font-family:"Roboto Condensed",sans-serif;font-size:26px;color:var(--green);padding-bottom:12px;border-bottom:1px solid #aaa}
.field{display:flex;align-items:center;justify-content:space-between;margin-top:12px;font-size:13px;font-weight:600}
.field span{width:196px;height:23px;border:1px solid #bbb;background:linear-gradient(#f4f4f4,#e6e6e6)}
.signup .field:first-of-type{margin-top:18px}
.actions{display:flex;justify-content:flex-end;gap:10px;margin-top:18px}
.actions span{height:34px;padding:0 12px;display:flex;align-items:center;color:#fff;font-size:13px}
.actions .login{background:#444}
.actions .join{background:var(--green)}
.forgot{text-align:right;color:var(--green);font-size:12px;margin-top:10px}

/* auctions */
.auctions{height:690px;background:var(--panel)}
.current{position:absolute;left:0;top:18px;width:708px}
.current .section-title::after,.suggested .section-title::after{content:"";flex:1;border-bottom:1px solid var(--green);margin-top:14px}
.pager{position:absolute;right:0;top:4px;display:flex;gap:6px}
.card{position:absolute;left:0;width:708px;height:186px;border:1px solid #ccc;background:#fafafa}
.card-img{position:absolute;left:11px;top:11px;width:204px;height:163px;border:1px solid #bbb}
.card h4{position:absolute;left:236px;top:14px;width:240px;font-weight:600;font-size:21px;line-height:24px;color:var(--green)}
.card .addr{position:absolute;right:10px;top:10px;text-align:right;font-size:15px;line-height:21px;color:#666}
.card .lead{position:absolute;left:236px;top:90px;font-size:16.5px;color:#111}
.card .quote{position:absolute;left:232px;top:126px;width:290px;font-size:13px;line-height:22px;color:#333}
.card .btn-sm{position:absolute;left:587px;top:115px}
.suggested{position:absolute;right:0;top:18px;width:322px}
.sugg-box{position:absolute;top:43px;left:0;width:320px;height:326px;border:1px solid #ccc;background:#fafafa}
.sugg{position:absolute;left:12px;width:300px;height:120px}
.sugg-img{position:absolute;left:0;top:0;width:129px;height:120px;border:1px solid #bbb;background:linear-gradient(#cfe0ee,#a7b7c4 45%,#7ea65a)}
.sugg h5{position:absolute;left:143px;top:4px;font-family:"Roboto Condensed",sans-serif;font-size:15px;line-height:20px;color:var(--green)}
.sugg p{position:absolute;left:143px;top:50px;font-size:13.5px;line-height:21px;color:#444}
.sugg .date{position:absolute;left:143px;top:100px;font-size:13.5px;color:#111}
.agent{position:absolute;right:0;top:404px;width:320px;height:233px;background:linear-gradient(160deg,#7d9bb8,#c7d2dc 50%,#2b3645)}
.agent-bar{position:absolute;left:0;right:0;bottom:0;height:40px;background:#111;display:flex;align-items:center;gap:18px;padding-left:10px;color:#fff}
.agent-bar b{font-family:"Roboto Condensed",sans-serif;font-size:26px;color:var(--green)}
.agent-bar span{font-size:14.5px}

/* tweet */
.tweet{height:82px;background:var(--white);position:relative}
.tweet-badge{position:absolute;left:50%;top:-22px;transform:translateX(-50%);width:92px;height:46px;background:#fff;border-radius:46px 46px 0 0;display:flex;justify-content:center;padding-top:12px}
.tweet p{position:absolute;top:30px;left:0;right:0;text-align:center;font-size:15.5px;color:#444}
.tweet p span{color:var(--sky)}

/* footer */
.site-footer{height:158px;background:linear-gradient(#e9e9e9,#e2e2e2)}
.foot-nav{position:absolute;top:30px;left:0;display:flex;font-size:13.5px;color:#444}
.foot-nav span+span::before{content:"/";color:#999;margin:0 11px}
.foot-nav span:first-child{color:var(--green)}
.foot-brand{position:absolute;left:0;top:80px}
.foot-brand .brand-name{font-size:28px}
.foot-brand .brand-tag{font-size:11px;color:var(--green);margin-top:2px;padding-left:8px}
.badges{position:absolute;right:0;top:34px;display:flex;gap:12px;align-items:flex-end}
.badges span{background:#222}
.copy{position:absolute;right:0;top:122px;font-size:12.5px;color:#555}
</style>
</head>
<body>

<header class="site-header">
  <div class="wrap">
    <div class="brand">
      <div class="brand-name">BELLWETHER</div>
      <div class="brand-tag" style="color:var(--green)">AUCTION &amp; MARKETING, LLC</div>
    </div>
    <div class="social" aria-label="Social links"><span></span><span></span><span></span><span></span><span></span></div>
    <div class="contact">
      <div>
        <svg width="24" height="26" viewBox="0 0 24 26"><path d="M6 2l4 5-2 3c1 3 3 6 7 8l3-2 4 4-3 4C9 23 2 13 3 4z" fill="var(--green)"/></svg>
        1-800-555-0142
      </div>
      <div>
        <svg width="28" height="22" viewBox="0 0 28 22"><rect x="1" y="3" width="26" height="18" fill="var(--green)"/><path d="M1 3l13 10L27 3" stroke="#fff" stroke-width="2" fill="none"/></svg>
        info@bellwether-auction.com
      </div>
    </div>
  </div>
</header>

<nav class="main-nav">
  <div class="wrap">
    <ul>
      <li class="active">Home</li><li>Auctions</li><li>Service</li><li>For Sale</li><li>About Us</li><li>Reid Video</li><li>News &amp; Events</li><li>Contact Us</li>
    </ul>
  </div>
</nav>

<section class="hero">
  <div class="hero-photo" role="img" aria-label="Slideshow photo: a hand holding a small house on a patch of lawn against a blue sky"></div>
  <div class="wrap">
    <svg class="hero-arrow" style="left:0" width="48" height="70" viewBox="0 0 48 70"><path d="M40 4L8 35l32 31" stroke="var(--green)" stroke-width="10" fill="none"/></svg>
    <svg class="hero-arrow" style="right:0" width="48" height="70" viewBox="0 0 48 70"><path d="M8 4l32 31L8 66" stroke="var(--green)" stroke-width="10" fill="none"/></svg>
  </div>
  <div class="hero-caption">Serving The Arkanasa &amp; Okhahoma Regions</div>
</section>

<section class="welcome">
  <div class="wrap">
    <h2>Welcome to our website</h2>
    <p>Lorem ipsum dolor sit amet, consectetur adipiscing elit. Phasellus blandit eu erat quis bibendum. Aenean dictum dapibus justo, a pharetra nisi gravida non. Sed rhoncus sapien ut leo blandit, et tristique leo aliquam. Donec in convallis erat, ac pulvinar turpis. Ut elit massa, pulvinar eget adipiscing ac, lacinia non ligula. Pellentesque bibendum euismod quam, id ornare nulla pellentesque vitae. Vivamus vitae adipiscing ante. Fusce nec accumsan odio. Nunc lobortis tortor a augue convallis fringilla.</p>
    <div class="go"><svg width="12" height="12" viewBox="0 0 12 12"><path d="M4 2l4 4-4 4" stroke="#fff" stroke-width="2.4" fill="none"/></svg></div>
    <div class="video" role="img" aria-label="Featured video: city skyline at night">
      <svg width="96" height="96" viewBox="0 0 96 96"><circle cx="48" cy="48" r="40" stroke="#aaa" stroke-width="9" fill="none" opacity=".8"/><circle cx="48" cy="48" r="25" fill="#999" opacity=".8"/><path d="M42 36l16 12-16 12z" fill="#333"/></svg>
    </div>
  </div>
</section>

<section class="testimonials">
  <div class="wrap">
    <h2 class="section-title">Testimonials</h2>
    <div class="t-photo" role="img" aria-label="Customer portrait"></div>
    <div class="t-name">Customor Name</div>
    <div class="t-lead">Lorem ipsum dolor sit amet, consectetur adipiscing elit. Sed a tempus ipsum.</div>
    <div class="t-quote">"Mapibus vulputate mattis. In elementum purus sem, at venenatis est adipiscing sit amet. Sed in sapien eget lacus consequat laoreet quis sit amet turpis. Maecenas tempus scelerisque felis congue tristique. Suspendisse commodo malesuada risus, ac rutrum felis tincidunt at. Sed in est vitae sem commodo laoreet."</div>
    <span class="btn-sm">Read more</span>

    <form class="signup">
      <h3>Join Our Email List</h3>
      <div class="field">User name<span></span></div>
      <div class="field">Password<span></span></div>
      <div class="field">Phone<span></span></div>
      <div class="actions"><span class="login">Log In</span><span class="join">Sing up</span></div>
      <div class="forgot">Forgot your login information?</div>
    </form>
  </div>
</section>

<section class="auctions">
  <div class="wrap">
    <div class="current">
      <h2 class="section-title">Current Auctions</h2>
      <div class="pager">
        <div class="go"><svg width="12" height="12" viewBox="0 0 12 12"><path d="M8 2L4 6l4 4" stroke="#fff" stroke-width="2.4" fill="none"/></svg></div>
        <div class="go"><svg width="12" height="12" viewBox="0 0 12 12"><path d="M4 2l4 4-4 4" stroke="#fff" stroke-width="2.4" fill="none"/></svg></div>
      </div>

      <article class="card" style="top:46px">
        <div class="card-img" role="img" aria-label="Row of suburban houses" style="background:linear-gradient(#cfe2f2,#b5bcc4 50%,#6fa04c)"></div>
        <h4>Constructions &amp; Shop Equiopment</h4>
        <div class="addr">214 North Elm<br>Street<br>Fairvale, EN</div>
        <div class="lead">Lorem ipsum dolor sit amet, consectetur</div>
        <div class="quote">"Mapibus vulputate mattis. In elementum at venenatis est adipiscing sit amet. Sed in</div>
        <span class="btn-sm">Read more</span>
      </article>

      <article class="card" style="top:244px">
        <div class="card-img" role="img" aria-label="City towers at dusk over water" style="background:linear-gradient(#2c3e6e,#5a6d93 50%,#2a2d3d)"></div>
        <h4>Constructions &amp; Shop Equiopment</h4>
        <div class="addr">214 North Elm<br>Street<br>Fairvale, EN</div>
        <div class="lead">Lorem ipsum dolor sit amet, consectetur</div>
        <div class="quote">"Mapibus vulputate mattis. In elementum at venenatis est adipiscing sit amet. Sed in</div>
        <span class="btn-sm">Read more</span>
      </article>

      <article class="card" style="top:442px">
        <div class="card-img" role="img" aria-label="Historic brick building" style="background:linear-gradient(#9cc2e8,#b0785c 50%,#7a4a38)"></div>
        <h4>Constructions &amp; Shop Equiopment</h4>
        <div class="addr">214 North Elm<br>Street<br>Fairvale, EN</div>
        <div class="lead">Lorem ipsum dolor sit amet, consectetur</div>
        <div class="quote">"Mapibus vulputate mattis. In elementum at venenatis est adipiscing sit amet. Sed in</div>
        <span class="btn-sm">Read more</span>
      </article>
    </div>

    <aside class="suggested">
      <h2 class="section-title">Suggested Auctions</h2>
      <div class="pager">
        <div class="go"><svg width="12" height="12" viewBox="0 0 12 12"><path d="M8 2L4 6l4 4" stroke="#fff" stroke-width="2.4" fill="none"/></svg></div>
        <div class="go"><svg width="12" height="12" viewBox="0 0 12 12"><path d="M4 2l4 4-4 4" stroke="#fff" stroke-width="2.4" fill="none"/></svg></div>
      </div>
      <div class="sugg-box">
        <div class="sugg" style="top:27px">
          <div class="sugg-img" role="img" aria-label="Suburban houses"></div>
          <h5>Estate Auction-<br>Halden Auction Center</h5>
          <p>Mapibusv uplutate attis<br>Mapibusv.</p>
          <div class="date">Auction Date:Jan 23, 2014</div>
        </div>
        <div class="sugg" style="top:178px">
          <div class="sugg-img" role="img" aria-label="Suburban houses"></div>
          <h5>Estate Auction-<br>Halden Auction Center</h5>
          <p>Mapibusv uplutate attis<br>Mapibusv.</p>
          <div class="date">Auction Date:Jan 23, 2014</div>
        </div>
      </div>
      <div class="agent" role="img" aria-label="Agent portrait in front of office towers">
        <div class="agent-bar"><b>Reid Calloway</b><span>Lience 000.482.1937</span></div>
      </div>
    </aside>
  </div>
</section>

<section class="tweet">
  <div class="tweet-badge"><svg width="30" height="30" viewBox="0 0 30 30"><circle cx="15" cy="15" r="13" fill="var(--sky)"/></svg></div>
  <p>Lorem ipsum dolor sit amet, consectetur adipiscing elit. Aenean hendrerit, tellus in fermentum pellentesque non turpis. <span>2 days ago</span></p>
</section>

<footer class="site-footer">
  <div class="wrap">
    <div class="foot-nav"><span>Home</span><span>Auctions</span><span>Service</span><span>For sale</span><span>About us</span><span>Reid Video</span><span>News &amp; Events</span><span>Contact us</span></div>
    <div class="foot-brand">
      <div class="brand-name">BELLWETHER</div>
      <div class="brand-tag">AUCTION &amp; MARKETING, LLC</div>
    </div>
    <div class="badges">
      <span style="width:42px;height:42px;background:#777"></span>
      <span style="width:42px;height:48px"></span>
      <span style="width:46px;height:52px"></span>
    </div>
    <div class="copy">© 2014 by Bellwether. All Rights Reserved</div>
  </div>
</footer>

</body>
</html>
```